Alpenmark Banner

Hi boys and girls :)

We have a little project 4u.

We need a banner in 4 sizes :

Leaderboard: 728*90
Wide SkyScraper: 160*600
Medium Rectangle: 300*250
Ribbon (special format): 990*45

Message on banner :

Either our Logo + Immigration, Integration, Naturalization

Or our Logo + Incorporation, Domicile, Secretarial Services

And if space allows for it www.alpenmark-example.com as well.

We are looking for a clean design, check our Website for inspiration concerning colors.

```html
<!DOCTYPE html>
<html lang="en">
<head>
<meta charset="utf-8">
<title>Alpenmark Banner Set</title>
<link rel="stylesheet" href="https://fonts.googleapis.com/css2?family=Marcellus&family=Marcellus+SC&display=swap">
<style>
  :root {
    --page: #f1f1f1;
    --red: #d90000;
    --red-deep: #a60000;
    --red-bright: #ff1414;
    --white: #ffffff;
    --charcoal: #333333;
    --brand-red: #b00d0d;
  }
  html, body { margin: 0; padding: 0; overflow: hidden; }
  body { width: 1200px; height: 1000px; background: var(--page); position: relative; }
  .banner { position: absolute; overflow: hidden; }
  .banner svg.decor { position: absolute; inset: 0; width: 100%; height: 100%; }
  .brand-name {
    position: absolute; font-family: "Marcellus", serif; font-weight: 400;
    letter-spacing: 0.02em; white-space: nowrap; line-height: 1;
  }
  .tagline {
    position: absolute; font-family: "Marcellus SC", serif; color: var(--white);
    white-space: nowrap; line-height: 1; letter-spacing: 0.03em;
  }

  .leaderboard { left: 75px; top: 38px; width: 1024px; height: 127px; background: var(--red); }
  .leaderboard .brand-name { left: 60px; top: 48px; font-size: 34px; color: var(--white); }
  .leaderboard .tagline { left: 517px; top: 57px; font-size: 15px; }

  .skyscraper { left: 134px; top: 201px; width: 206px; height: 771px; background: var(--red); }
  .skyscraper .brand-name { left: 0; width: 206px; text-align: center; top: 512px; top: 512px; top: 510px; top: 330px; font-size: 32px; color: var(--white); }
  .skyscraper .tagline-stack { position: absolute; left: 0; width: 206px; top: 592px; text-align: center; }
  .skyscraper .tagline-stack .tagline { position: static; display: block; font-size: 13px; margin-bottom: 10px; }

  .rectangle { left: 422px; top: 252px; width: 426px; height: 355px; background: var(--white); }
  .rectangle .brand-name { left: 0; width: 426px; text-align: center; top: 150px; font-size: 58px; color: var(--brand-red); }

  .seal { position: absolute; left: 550px; top: 700px; width: 190px; height: 100px; }

  .corner-mark { position: absolute; left: 975px; top: 905px; width: 165px; text-align: center; }
  .corner-mark .brand-name { position: static; font-size: 30px; color: var(--brand-red); }
</style>
</head>
<body>

  <section class="banner leaderboard" aria-label="Leaderboard banner">
    <svg class="decor" viewBox="0 0 1024 127" preserveAspectRatio="none" aria-hidden="true">
      <path d="M0,30 Q18,8 60,0 L44,0 Q12,8 0,18 Z" fill="var(--white)"/>
      <path d="M770,127 Q955,118 995,0 L1024,0 L1024,127 Z" fill="var(--white)"/>
      <path d="M815,127 Q975,112 1024,10 L1024,127 Z" fill="var(--red-deep)"/>
      <path d="M870,127 Q995,112 1024,45 L1024,127 Z" fill="var(--red-bright)"/>
    </svg>
    <span class="brand-name">Alpenmark</span>
    <span class="tagline">Immigration, Integration, Naturalization</span>
  </section>

  <section class="banner skyscraper" aria-label="Wide skyscraper banner">
    <svg class="decor" viewBox="0 0 206 771" preserveAspectRatio="none" aria-hidden="true">
      <path d="M0,0 L120,0 Q40,12 0,42 Z" fill="var(--red-bright)"/>
      <path d="M0,42 Q40,14 120,0 L135,0 Q55,16 0,54 Z" fill="var(--white)"/>
      <path d="M0,54 Q55,16 135,0 L150,0 Q70,16 0,62 Z" fill="var(--red-deep)"/>
      <path d="M30,771 Q170,730 206,620 L206,771 Z" fill="var(--white)"/>
      <path d="M60,771 Q185,725 206,660 L206,771 Z" fill="var(--red-deep)"/>
      <path d="M100,771 Q195,735 206,700 L206,771 Z" fill="var(--red-bright)"/>
    </svg>
    <span class="brand-name">Alpenmark</span>
    <div class="tagline-stack">
      <span class="tagline">Immigration</span>
      <span class="tagline">Integration</span>
      <span class="tagline">Naturalization</span>
    </div>
  </section>

  <section class="banner rectangle" aria-label="Medium rectangle banner">
    <svg class="decor" viewBox="0 0 426 355" preserveAspectRatio="none" aria-hidden="true">
      <path d="M0,0 L120,0 Q40,14 0,48 Z" fill="var(--red)"/>
      <path d="M0,48 Q40,14 120,0 L128,0 Q48,18 0,56 Z" fill="var(--white)"/>
      <path d="M0,60 Q50,20 135,0 L140,0 Q55,22 0,66 Z" fill="var(--charcoal)"/>
      <path d="M250,355 Q390,320 426,225 L426,232 Q392,326 262,355 Z" fill="var(--charcoal)"/>
      <path d="M285,355 Q400,320 426,270 L426,355 Z" fill="var(--red-deep)"/>
      <path d="M330,355 Q410,330 426,300 L426,355 Z" fill="var(--red-bright)"/>
    </svg>
    <span class="brand-name">Alpenmark</span>
  </section>

  <svg class="seal" viewBox="0 0 190 100" aria-label="Ribbon seal">
    <path d="M0,26 L55,26 L55,74 L0,74 L16,50 Z" fill="var(--red)"/>
    <path d="M190,26 L135,26 L135,74 L190,74 L174,50 Z" fill="var(--red)"/>
    <rect x="30" y="30" width="130" height="40" fill="var(--red)"/>
    <line x1="30" y1="35" x2="160" y2="35" stroke="var(--white)" stroke-width="1"/>
    <line x1="30" y1="65" x2="160" y2="65" stroke="var(--white)" stroke-width="1"/>
    <circle cx="95" cy="50" r="46" fill="var(--red-deep)"/>
    <circle cx="95" cy="50" r="38" fill="var(--red)" stroke="var(--white)" stroke-width="2"/>
  </svg>

  <div class="corner-mark">
    <span class="brand-name">Alpenmark</span>
  </div>

</body>
</html>
```